Restaurant Menu for beach club in Martinique

We would like to set a new design for our Menu. We are a restaurant, and beach club, located in Martinique. Our website is available at : http://www.corailventmer.com Regards

Colors

Designer to choose colors to be used in the design.

```html
<!DOCTYPE html>
<html lang="fr">
<head>
<meta charset="utf-8">
<title>Corail Vent Mer – Menu</title>
<link rel="stylesheet" href="https://fonts.googleapis.com/css2?family=Amatic+SC:wght@700&family=Fira+Sans:wght@400;500&display=swap">
<style>
  :root{
    --stage:#2b2b2b;
    --cream:#f5dcbc;
    --jungle:#163a1f;
    --leaf:#3f7a32;
    --leaf-light:#7fae45;
    --orange:#e0522a;
    --olive:#8c9a5c;
    --ink:#1e2a17;
    --desc:#6e7d3d;
    --white:#ffffff;
  }
  *{margin:0;padding:0;box-sizing:border-box}
  html,body{width:1200px;height:575px;overflow:hidden;background:var(--stage)}
  .canvas{position:relative;width:1200px;height:575px;background:var(--stage)}
  .page{position:absolute;top:29px;width:366px;height:518px;overflow:hidden}
  .page--cover{left:28px;background:var(--jungle)}
  .page--starters{left:416px;background:var(--cream)}
  .page--mains{left:804px;background:var(--cream)}
  .foliage{position:absolute;left:0;top:0;width:366px;height:518px}

  .brand{position:absolute;left:0;width:366px;text-align:center;color:var(--white);font-family:'Fira Sans',sans-serif}
  .brand__name{top:168px;font-size:26px;font-weight:500;letter-spacing:1px}
  .brand__place{top:215px;font-size:7px;font-weight:400;letter-spacing:3px}
  .brand__rule{position:absolute;top:222px;left:68px;width:230px;height:1px;background:var(--white)}
  .brand__rule span{display:none}
  .cover__restaurant{position:absolute;top:264px;left:0;width:366px;text-align:center;font-family:'Amatic SC',cursive;font-weight:700;font-size:38px;color:var(--orange);letter-spacing:1px}
  .cover__menu{position:absolute;top:322px;left:0;width:366px;text-align:center;font-family:'Amatic SC',cursive;font-weight:700;font-size:118px;line-height:1;color:var(--olive);letter-spacing:4px}

  .section-title{position:absolute;left:0;width:366px;text-align:center;font-family:'Amatic SC',cursive;font-weight:700;color:var(--orange);line-height:1}
  .page--starters .section-title{top:72px;font-size:44px}
  .page--mains .section-title{top:16px;font-size:42px}

  .dish{position:absolute;left:0;width:366px;text-align:center;font-family:'Fira Sans',sans-serif}
  .dish__name{font-size:10.5px;font-weight:500;color:var(--ink);line-height:12px}
  .dish__detail{font-size:5.6px;color:var(--desc);line-height:7.5px}
  .dish__price{font-size:7px;color:var(--ink);margin-left:4px}
</style>
</head>
<body>
<div class="canvas">

  <section class="page page--cover">
    <svg class="foliage" viewBox="0 0 366 518" role="img" aria-label="Tropical leaves and bird-of-paradise flowers framing the cover">
      <defs>
        <radialGradient id="coverLeaves" cx="50%" cy="50%" r="70%">
          <stop offset="0.35" stop-color="#163a1f"/>
          <stop offset="0.75" stop-color="#2f6b2a"/>
          <stop offset="1" stop-color="#5e9a3a"/>
        </radialGradient>
      </defs>
      <rect width="366" height="518" fill="url(#coverLeaves)"/>
    </svg>
    <div class="brand brand__name">Corail Vent Mer</div>
    <div class="brand__rule"></div>
    <div class="brand brand__place">MARTINIQUE</div>
    <div class="cover__restaurant">Restaurant</div>
    <div class="cover__menu">MENU</div>
  </section>

  <section class="page page--starters">
    <svg class="foliage" viewBox="0 0 366 518" role="img" aria-label="Tropical leaves and bird-of-paradise flowers across the top corners">
      <defs>
        <linearGradient id="topLeaves" x1="0" y1="0" x2="0" y2="1">
          <stop offset="0" stop-color="#2e6a2c"/>
          <stop offset="1" stop-color="#6a9e3e"/>
        </linearGradient>
      </defs>
      <path d="M0 0H366V200C340 190 330 150 300 120C270 90 230 70 200 55C170 45 140 60 110 70C80 80 60 110 40 150C25 180 10 180 0 170Z" fill="url(#topLeaves)"/>
    </svg>
    <h2 class="section-title">Les Entrées</h2>
    <div class="dish" style="top:134px"><div class="dish__name">L’ assiette «zen»</div><div class="dish__detail">(nem de gambas, maki au saumon, mini brochette de poulet,<br>samoussa au chèvre frais)<span class="dish__price">9,80 €</span></div></div>
    <div class="dish" style="top:173px"><div class="dish__name">Les nems aux deux saumons</div><div class="dish__detail">sauce crémeuse au wasabi et salade de pousses d’épinards<span class="dish__price">9,50 €</span></div></div>
    <div class="dish" style="top:207px"><div class="dish__name">La salade du «Périgord»</div><div class="dish__detail">(Salade, roquette, oignons rouges, foie gras maison, gésiers confits, magrets fumés et pommes)<span class="dish__price">13,10 €</span></div></div>
    <div class="dish" style="top:240px"><div class="dish__name">Le tartare de loup à la moutarde de Reims</div><div class="dish__detail">sur une gelée de concombres<span class="dish__price">10,50 €</span></div></div>
    <div class="dish" style="top:273px"><div class="dish__name">Le bavarois de tomates</div><div class="dish__detail">farci au chèvre frais et jus de betteraves<span class="dish__price">8,20 €</span></div></div>
    <div class="dish" style="top:306px"><div class="dish__name">Le royal de foie gras</div><div class="dish__detail">et rouleau de printemps au poulet et vermicelles<span class="dish__price">10,50 €</span></div></div>
    <div class="dish" style="top:340px"><div class="dish__name">Le tartare de St Jacques</div><div class="dish__detail">aux échalotes rôties et concombres<span class="dish__price">12,50 €</span></div></div>
    <div class="dish" style="top:373px"><div class="dish__name">L’oeuf “cocotte”</div><div class="dish__detail">à la crème de morilles et jambon ibérique<span class="dish__price">9,50 €</span></div></div>
    <div class="dish" style="top:406px"><div class="dish__name">La salade de légumes</div><div class="dish__detail">croquants et gambas façon thaï<span class="dish__price">9,80 €</span></div></div>
    <div class="dish" style="top:439px"><div class="dish__name">Le foie gras de canard</div><div class="dish__detail">au vieux porto, brioche maison<span class="dish__price">13,80 €</span></div></div>
    <div class="dish" style="top:473px"><div class="dish__name">Le gâteau de lapereau</div><div class="dish__detail">au lard paysan, farci au foie gras, compote d’oignons rouges<span class="dish__price">9,80 €</span></div></div>
  </section>

  <section class="page page--mains">
    <svg class="foliage" viewBox="0 0 366 518" role="img" aria-label="Tropical leaves and bird-of-paradise flowers along the bottom edge">
      <defs>
        <linearGradient id="bottomLeaves" x1="0" y1="0" x2="0" y2="1">
          <stop offset="0" stop-color="#6a9e3e"/>
          <stop offset="1" stop-color="#2a5e28"/>
        </linearGradient>
      </defs>
      <path d="M0 500C10 470 30 450 50 440C70 420 80 400 100 390C115 430 125 460 140 450C160 440 190 450 210 445C230 435 250 420 270 430C290 420 310 425 330 440C345 450 358 460 366 470V518H0Z" fill="url(#bottomLeaves)"/>
    </svg>
    <h2 class="section-title">Les Plats</h2>
    <div class="dish" style="top:77px"><div class="dish__name">L’ assiette «zen»</div><div class="dish__detail">(nem de gambas, maki au saumon, mini brochette de poulet, samoussa au chèvre frais)<span class="dish__price">9,80 €</span></div></div>
    <div class="dish" style="top:111px"><div class="dish__name">Les nems aux deux saumons</div><div class="dish__detail">sauce crémeuse au wasabi et salade de pousses d’épinards<span class="dish__price">9,50 €</span></div></div>
    <div class="dish" style="top:144px"><div class="dish__name">La salade du «Périgord»</div><div class="dish__detail">(Salade, roquette, oignons rouges, foie gras maison, gésiers confits, magrets fumés et pommes)<span class="dish__price">13,10 €</span></div></div>
    <div class="dish" style="top:177px"><div class="dish__name">Le tartare de loup à la moutarde de Reims</div><div class="dish__detail">sur une gelée de concombres<span class="dish__price">10,50 €</span></div></div>
    <div class="dish" style="top:210px"><div class="dish__name">Le bavarois de tomates</div><div class="dish__detail">farci au chèvre frais et jus de betteraves<span class="dish__price">8,20 €</span></div></div>
    <div class="dish" style="top:243px"><div class="dish__name">Le royal de foie gras</div><div class="dish__detail">et rouleau de printemps au poulet et vermicelles<span class="dish__price">10,50 €</span></div></div>
    <div class="dish" style="top:277px"><div class="dish__name">Le tartare de St Jacques</div><div class="dish__detail">aux échalotes rôties et concombres<span class="dish__price">12,50 €</span></div></div>
    <div class="dish" style="top:310px"><div class="dish__name">L’oeuf “cocotte”</div><div class="dish__detail">à la crème de morilles et jambon ibérique<span class="dish__price">9,50 €</span></div></div>
    <div class="dish" style="top:343px"><div class="dish__name">Le gâteau de lapereau</div><div class="dish__detail">au lard paysan, farci au foie gras, compote d’oignons rouges<span class="dish__price">9,80 €</span></div></div>
    <div class="dish" style="top:377px"><div class="dish__name">Le foie gras de canard</div><div class="dish__detail">au vieux porto, brioche maison<span class="dish__price">13,80 €</span></div></div>
    <div class="dish" style="top:410px"><div class="dish__name">La salade de légumes</div><div class="dish__detail">croquants et gambas façon thaï<span class="dish__price">9,80 €</span></div></div>
  </section>

</div>
</body>
</html>
```